Rudy Fenwick - Free Personalised Health Consultation - "One size does not fit all"

This flyer will be left on tables/seats at speaking events and seminars and used to attain leads.

Top half will have "SMS me for a FREE Personalised Health Consultation" and my picture (see www.rudyfenwick.example and pick most engaging photo) and underneath my contact details. It must have lines with "Notes:" halfway down so people can take notes at the seminar and lines on the back with my contact details again and "Notes: with lines.

I am having a business card also being designed by Artshelf for same and would like the flyer and business card to carry a similar feel/look for consistency.

Below is the brief for the business card being designed:
Business Card for www.rudyfenwick.example site. It is a trust site and I use it for 1:1 relatable connections. It is the one I use for building intimate 1:1 trust building and Exec Coaching Services and programs for high wealth individuals and corporates. I also have a commercial programmatic site of my personal health products and services and programs for main stream one to many. www.quietbirchliving.example that can also provoke thought for the www.rudyfenwick.example business card. (mind you will get a separate business card for that site, but want to provide context). It has a logo which you may want to draw from in designing the rudyfenwick business card which is personal and is about building my brand. There is also a rudyfenwick personal FB page and rudyfenwick business FB page. I am a Certified Talent Compass 3.1 Coach with Harlow and you can get a corporate brief of me on there to give you more context https://www.harlowtalenthub.example/coach/en-us/directory?search=rudy

Target Market(s)

Exec, IT, Health conscious. Corporates wanting to run Health and Wellness programs. Those wanting to go from good to great. Millennials to Middleaged.

Industry/Entity Type

Health And Wellness

Font styles to use
Sans Serif
Other font styles liked:
• Arial and Calibri ok too

Colors

Designer to choose colors to be used in the design.

Requirements
Must have
• Picture of me - use best from www.rudyfenwick.example or can send one you choose.
• Contact details like my buisness card being designed by you guys in separate project.
• Name: Rudy Fenwick
• email: rudy@rudyfenwick.,example
• Phone: Australia +61 400 000 000 Singapore: +65 9000 0000
Nice to have
• Open to ideas

```html
<!DOCTYPE html>
<html lang="en">
<head>
<meta charset="utf-8">
<title>Rudy Fenwick – Seminar Notes Flyer</title>
<link rel="stylesheet" href="https://fonts.googleapis.com/css2?family=Oswald:wght@500&family=Roboto:wght@400;500;700&display=swap">
<style>
  :root {
    --canvas: #e8e6e3;
    --paper: #ffffff;
    --charcoal: #282828;
    --slate: #7b7b7b;
    --ink: #1c1c1c;
    --rule: #8a8a8a;
    --photo-light: #d9d9d9;
    --photo-dark: #5a5a5a;
  }
  * { margin: 0; padding: 0; box-sizing: border-box; }
  html, body { width: 1200px; height: 903px; overflow: hidden; }
  body {
    background: var(--canvas);
    position: relative;
    font-family: "Roboto", Arial, sans-serif;
    color: var(--ink);
  }
  .flyer {
    position: absolute;
    top: 80px;
    width: 526px;
    height: 743px;
    background: var(--paper);
    box-shadow: 0 2px 8px rgba(0,0,0,0.18);
    overflow: hidden;
  }
  .flyer--front { left: 58px; }
  .flyer--back { left: 617px; }

  .hero { position: absolute; left: 0; top: 0; width: 526px; height: 386px; }
  .hero svg { display: block; }
  .hero__headline {
    position: absolute; left: 24px; top: 0; width: 202px;
    color: #fff;
  }
  .headline__lead {
    position: absolute; top: 82px; left: 0;
    font-family: "Oswald", "Arial Narrow", sans-serif;
    font-weight: 500; font-size: 40px; line-height: 1;
    white-space: nowrap; letter-spacing: -0.3px;
  }
  .headline__free {
    position: absolute; top: 128px; left: -3px;
    font-family: "Oswald", "Arial Narrow", sans-serif;
    font-weight: 500; font-size: 122px; line-height: 1;
    letter-spacing: 1px;
  }
  .headline__offer {
    position: absolute; top: 246px; left: 0;
    font-weight: 700; font-size: 25.5px; line-height: 1; white-space: nowrap;
  }
  .headline__topic {
    position: absolute; top: 280px; left: 0;
    font-weight: 500; font-size: 17.3px; line-height: 1; white-space: nowrap;
  }
  .headline__signoff {
    position: absolute; top: 312px; left: 89px;
    font-weight: 400; font-size: 16px; line-height: 1; white-space: nowrap;
  }

  .notes { position: absolute; left: 24px; right: 25px; }
  .notes__title { font-size: 20px; font-weight: 400; line-height: 1; letter-spacing: 0.3px; }
  .notes__line { border-top: 1px dotted var(--rule); }
  .flyer--front .notes { top: 445px; }
  .flyer--front .notes__line { margin-top: 40.5px; }
  .flyer--front .notes__line:first-of-type { margin-top: 21px; }
  .flyer--back .notes { top: 27px; left: 23px; right: 24px; }
  .flyer--back .notes__line { margin-top: 39.6px; }
  .flyer--back .notes__line:first-of-type { margin-top: 19px; }

  .contact-bar { position: absolute; left: 0; bottom: 0; width: 526px; height: 41px; }
  .contact-bar svg { position: absolute; left: 0; top: 0; }
  .contact-bar__item {
    position: absolute; top: 0; height: 41px; line-height: 41px;
    color: #fff; font-size: 12px; font-weight: 500; white-space: nowrap;
  }
  .contact-bar__au { left: 30px; }
  .contact-bar__divider { position: absolute; left: 175px; top: 9px; width: 1px; height: 22px; background: #9a9a9a; }
  .contact-bar__sg { left: 183px; }
  .contact-bar__email { left: 356px; width: 160px; text-align: center; line-height: 38px; }
</style>
</head>
<body>

<article class="flyer flyer--front">
  <header class="hero">
    <svg width="526" height="386" viewBox="0 0 526 386">
      <defs>
        <linearGradient id="photoTone" x1="0" y1="0" x2="1" y2="1">
          <stop offset="0" stop-color="var(--photo-light)"/>
          <stop offset="0.55" stop-color="#9a9a9a"/>
          <stop offset="1" stop-color="var(--photo-dark)"/>
        </linearGradient>
      </defs>
      <rect x="210" y="0" width="316" height="386" fill="url(#photoTone)" role="img" aria-label="Black and white photo of Rudy Fenwick in a dark suit, leaning on a bench beside a bicycle in a bright colonnade"/>
      <polygon points="0,0 220,0 290,152 252,386 0,386" fill="#fff"/>
      <polygon points="0,0 216,0 284,152 246,386 0,386" fill="var(--charcoal)"/>
    </svg>
    <div class="hero__headline">
      <p class="headline__lead">SMS me for a</p>
      <p class="headline__free">FREE</p>
      <p class="headline__offer">PERSONALISED</p>
      <p class="headline__topic">HEALTH CONSULTATION</p>
      <p class="headline__signoff">- Rudy Fenwick</p>
    </div>
  </header>

  <section class="notes">
    <h2 class="notes__title">NOTES</h2>
    <div class="notes__line"></div>
    <div class="notes__line"></div>
    <div class="notes__line"></div>
    <div class="notes__line"></div>
    <div class="notes__line"></div>
  </section>

  <footer class="contact-bar">
    <svg width="526" height="41" viewBox="0 0 526 41">
      <polygon points="0,0 345,0 331,41 0,41" fill="var(--charcoal)"/>
      <polygon points="349,0 526,0 526,41 335,41" fill="var(--slate)"/>
    </svg>
    <span class="contact-bar__item contact-bar__au">Australia +61 400 000 000</span>
    <span class="contact-bar__divider"></span>
    <span class="contact-bar__item contact-bar__sg">Singapore: +65 9000 0000</span>
    <span class="contact-bar__item contact-bar__email">rudy@rudyfenwick.example</span>
  </footer>
</article>

<article class="flyer flyer--back">
  <section class="notes">
    <h2 class="notes__title">NOTES</h2>
    <div class="notes__line"></div>
    <div class="notes__line"></div>
    <div class="notes__line"></div>
    <div class="notes__line"></div>
    <div class="notes__line"></div>
    <div class="notes__line"></div>
    <div class="notes__line"></div>
    <div class="notes__line"></div>
    <div class="notes__line"></div>
    <div class="notes__line"></div>
    <div class="notes__line"></div>
    <div class="notes__line"></div>
    <div class="notes__line"></div>
    <div class="notes__line"></div>
    <div class="notes__line"></div>
  </section>

  <footer class="contact-bar">
    <svg width="526" height="41" viewBox="0 0 526 41">
      <polygon points="0,0 345,0 331,41 0,41" fill="var(--charcoal)"/>
      <polygon points="349,0 526,0 526,41 335,41" fill="var(--slate)"/>
    </svg>
    <span class="contact-bar__item contact-bar__au">Australia +61 400 000 000</span>
    <span class="contact-bar__divider"></span>
    <span class="contact-bar__item contact-bar__sg">Singapore: +65 9000 0000</span>
    <span class="contact-bar__item contact-bar__email">rudy@rudyfenwick.example</span>
  </footer>
</article>

</body>
</html>
```